Website for boutique digital agency helping high-tech startups accelerate growth.

We need a website design for a relatively young company based in Mauritius called 'LoomTrax'.

We are a professional services firm delivering digital infrastructure for revenue operations (RevOps)*.

Entrepreneurial startups and SMBs in the technology sector work with us to accelerate growth by delivering extraordinary customer experiences across the full customer lifecycle.

We would like a colourful design that utilises the (4) colours of our existing logo design.

The final design should communicate dynamic growth through relentless customer focus.
----------------------------------------------------------
*Revenue Operations (RevOps) is the strategic alignment of sales, marketing and customer success operations to accelerate growth by delivering extraordinary customer experiences across the full customer life cycle.
Updates

Target Market(s)

Entrepreneurial startups and SMBs (Small/Medium Businesses) in the technology sector.

Question: Why the technology sector?

Answer: Because technology entrepreneurs often have a tremendous challenge to effectively communicate to the market and to prospective customers the value and the benefits of their products & services due to the inherent complexity of technological innovation.

LoomTrax is a team of creatively-minded engineers and technologists who have worked with and understand the technologies and innovations our clients are passionate about bringing to market.

Industry/Entity Type

Professional Service

Number of Pages Required

5+ page

Font styles to use
Sans Serif

Requirements
Must have
• Minimalistic designs rich with visual meaning are highly preferred. Mobile responsive designs are also required. Must show how designs render on Desktop, Tablet and Smartphone devices.

Website pages:
1) Homepage: problem statement, target customers, value proposition & benefits
2) Services: 3-4 tiers of services packages with pricing and "how to work with us"
3) Resources: links to all kinds of relevant materials
4) Contact Us: contact form and special project quote form
5) Blog: matrix design with featured images for each post
Nice to have
• Bold, interesting, colourful, inspiring images that visually communicate:
- relentless customer focus
- extraordinary, memorable experiences
- business at the speed of innovation
Should not have
• Any meme or theme that panders to "political correctness".

```html
<!DOCTYPE html>
<html lang="en">
<head>
<meta charset="utf-8">
<title>LoomTrax — Revenue Operations</title>
<link href="https://fonts.googleapis.com/css2?family=Montserrat:wght@700;800&family=Josefin+Sans:wght@400;600;700&display=swap" rel="stylesheet">
<style>
:root{
  --ink:#2a2d3e;
  --muted:#6b6f80;
  --blue:#1f2fd0;
  --green:#7ab82a;
  --teal:#1a7f78;
  --red:#f2163a;
  --orange:#f9650f;
  --contact:#4a55f0;
  --field:#2630cf;
  --soft-green:#cfe8a8;
}
*{box-sizing:border-box;margin:0;padding:0}
html,body{width:1200px;height:4231px;overflow:hidden;background:#fff}
body{position:relative;font-family:"Josefin Sans",sans-serif;color:var(--ink)}
a{color:inherit;text-decoration:none}

.section{position:absolute;left:0;width:1200px;height:658px}
.brand{position:absolute;left:85px;top:58px;display:flex;align-items:center;gap:8px;font-weight:700;font-size:17px;color:var(--ink)}
.brand-dot{width:12px;height:12px;border-radius:50%;background:var(--green)}

.nav{position:absolute;top:54px;left:678px;display:flex;gap:30px;font-size:14px;font-weight:600}
.nav a{padding-bottom:5px}
.nav .current{border-bottom:2px solid var(--ink)}

.side-menu{position:absolute;left:114px;top:195px;list-style:none}
.side-menu li{height:40px;display:flex;align-items:center;font-size:14px;font-weight:600;position:relative}
.side-menu li.active{font-size:21px;font-weight:700;height:46px}
.side-menu .num{position:absolute;left:-30px;top:2px;font-family:"Montserrat",sans-serif;font-size:28px;font-weight:800;opacity:.35}

.content{position:absolute;left:395px;width:325px}
.content h2{font-family:"Montserrat",sans-serif;font-weight:800;font-size:29px;line-height:37px;letter-spacing:.5px;margin-bottom:8px}
.content p{font-size:14px;line-height:18px;margin-bottom:16px}
.btn{display:inline-flex;align-items:center;justify-content:center;width:159px;height:48px;border-radius:7px;color:#fff;font-weight:600;font-size:14px;margin-top:14px}

.art{position:absolute;left:757px;width:328px;height:192px;border-radius:10px}

.contact{position:absolute;left:85px;top:3349px;width:1000px;height:363px;background:var(--contact);border-radius:14px}
.contact h2{position:absolute;left:85px;top:74px;font-family:"Montserrat",sans-serif;font-weight:800;font-size:40px;color:#fff;letter-spacing:1px}
.contact .people{position:absolute;left:75px;top:175px;width:420px;height:188px;border-radius:10px 10px 0 0;background:linear-gradient(180deg,#5b66f5,#3b3f66)}
.field{position:absolute;left:589px;width:326px;background:var(--field);border-radius:4px;color:#aeb4ff;font-size:11px;padding:12px 16px}
.send{position:absolute;left:589px;top:290px;width:110px;height:43px;border-radius:6px;background:var(--field);color:#fff;font-weight:600;font-size:14px;display:flex;align-items:center;justify-content:center}

.footer-brand{top:3872px;left:96px}
.footer-contact{position:absolute;left:87px;top:3952px;font-size:11px;font-weight:700;line-height:14px}
.footer-contact div{display:flex;gap:10px;align-items:flex-start;margin-bottom:16px}
.fcol{position:absolute;top:3876px;list-style:none;font-size:10px;color:var(--muted)}
.fcol h3{font-size:12px;font-weight:700;color:var(--ink);margin-bottom:16px}
.fcol li{height:21px}
.social{position:absolute;top:3880px;left:957px;display:flex;gap:14px}
.social span{width:32px;height:32px;border-radius:50%;background:var(--soft-green);display:block}
.copyright{position:absolute;top:4074px;left:0;width:1168px;text-align:center;font-size:12px;font-weight:600}
</style>
</head>
<body>

<section class="section" style="top:0">
  <div class="brand"><span class="brand-dot"></span>loomtrax.io</div>
  <nav class="nav"><a class="current">Home</a><a>Services</a><a>Resources</a><a>Contact Us</a><a>Blog</a></nav>
  <ul class="side-menu" style="top:235px">
    <li class="active"><span class="num" style="color:var(--blue)">01</span>Home</li>
    <li>Problem Statement</li><li>Target Customers</li><li>Value Proposition</li><li>Benefits</li>
  </ul>
  <div class="content" style="top:178px">
    <h2>What is RevOps</h2>
    <p>Revenue Operations, or RevOps, is a new department that manages full funnel operations across Marketing, Sales, and Customer Success.</p>
    <p>RevOps brings together four areas of responsibility from departmental silos: Operations, Enablement, Insights, and Tools</p>
    <a class="btn" style="background:var(--blue)">Get Started</a>
  </div>
  <div class="art" role="img" aria-label="Illustration of a laptop and phone with dashboards" style="top:232px;background:linear-gradient(135deg,#2a36d8,#c9ccf5)"></div>
</section>

<section class="section" style="top:658px">
  <div class="brand"><span class="brand-dot"></span>loomtrax.io</div>
  <nav class="nav"><a class="current">Home</a><a>Services</a><a>Resources</a><a>Contact Us</a><a>Blog</a></nav>
  <ul class="side-menu" style="top:225px">
    <li>Home</li>
    <li class="active"><span class="num" style="color:var(--green)">02</span>Problem Statement</li>
    <li>Target Customers</li><li>Value Proposition</li><li>Benefits</li>
  </ul>
  <div class="content" style="top:212px">
    <h2>RevOps Aligns<br>Everyone</h2>
    <p>RevOps keeps Marketing, Sales, and Customer Success aligned around the customer – unifying metrics, tech ownership, and change management.</p>
    <a class="btn" style="background:var(--green)">Learn More</a>
  </div>
  <div class="art" role="img" aria-label="Illustration of a globe with location pins" style="top:232px;background:radial-gradient(circle at 50% 55%,#7ab82a 0 32%,#eef6e2 33% 100%)"></div>
</section>

<section class="section" style="top:1316px">
  <div class="brand"><span class="brand-dot"></span>loomtrax.io</div>
  <nav class="nav"><a class="current">Home</a><a>Services</a><a>Resources</a><a>Contact Us</a><a>Blog</a></nav>
  <ul class="side-menu" style="top:225px">
    <li>Home</li><li>Problem Statement</li>
    <li class="active"><span class="num" style="color:var(--teal)">03</span>Target Customers</li>
    <li>Value Proposition</li><li>Benefits</li>
  </ul>
  <div class="content" style="top:200px">
    <h2>RevOps Creates<br>Focus</h2>
    <p>RevOps has four areas of responsibility: Operations, Enablement, Insights, and Tools. This creates focus by separating the management of internal and external stakeholders.</p>
    <a class="btn" style="background:var(--teal)">Learn More</a>
  </div>
  <div class="art" role="img" aria-label="Illustration of a person working at a laptop" style="top:228px;background:linear-gradient(180deg,#eceef3,#3f3d56)"></div>
</section>

<section class="section" style="top:1974px">
  <div class="brand"><span class="brand-dot"></span>loomtrax.io</div>
  <nav class="nav"><a class="current">Home</a><a>Services</a><a>Resources</a><a>Contact Us</a><a>Blog</a></nav>
  <ul class="side-menu" style="top:225px">
    <li>Home</li><li>Problem Statement</li><li>Target Customers</li>
    <li class="active"><span class="num" style="color:var(--red)">04</span>Value Proposition</li>
    <li>Benefits</li>
  </ul>
  <div class="content" style="top:192px">
    <h2>RevOps Simplifies<br>Everything</h2>
    <p>Most companies have legacy org structures based on how businesses were run twenty years ago. New functions have been added into this structure over time, creating leadership roles that are overly broad. RevOps consolidates operations into one team to simplify everything.</p>
    <a class="btn" style="background:var(--red)">Learn More</a>
  </div>
  <div class="art" role="img" aria-label="Illustration of a person sitting beside a large screen" style="top:256px;background:linear-gradient(135deg,#f2163a,#3f3d56)"></div>
</section>

<section class="section" style="top:2632px">
  <div class="brand"><span class="brand-dot"></span>loomtrax.io</div>
  <nav class="nav"><a class="current">Home</a><a>Services</a><a>Resources</a><a>Contact Us</a><a>Blog</a></nav>
  <ul class="side-menu" style="top:225px">
    <li>Home</li><li>Problem Statement</li><li>Target Customers</li><li>Value Proposition</li>
    <li class="active"><span class="num" style="color:var(--orange)">05</span>Benefits</li>
  </ul>
  <div class="content" style="top:214px">
    <h2>Getting Started<br>With RevOps</h2>
    <p>RevOps can start in two ways: distributed capabilities throughout your team, or specialized roles in a department. The right way to start depends upon your business model and company size.</p>
    <a class="btn" style="background:var(--orange)">Learn More</a>
  </div>
  <div class="art" role="img" aria-label="Illustration of a tilted dashboard with timeline bars" style="top:216px;background:linear-gradient(160deg,#fdf3ec,#f4f4f7)"></div>
</section>

<section class="contact">
  <h2>Contact Us</h2>
  <div class="people" role="img" aria-label="Illustration of two people working on laptops"></div>
  <div class="field" style="top:61px;height:40px">Name</div>
  <div class="field" style="top:122px;height:40px">Email</div>
  <div class="field" style="top:183px;height:75px">Message</div>
  <a class="send">Send</a>
</section>

<footer>
  <div class="brand footer-brand"><span class="brand-dot"></span>loomtrax.io</div>
  <div class="footer-contact">
    <div><svg width="12" height="14" viewBox="0 0 12 14"><path d="M6 13C2 8 1 6.5 1 5a5 5 0 0 1 10 0c0 1.5-1 3-5 8z" fill="none" stroke="#7ab82a" stroke-width="1.6"/><circle cx="6" cy="5" r="1.8" fill="#7ab82a"/></svg><span>48 Harbour Lane,<br>Port Louis, Mauritius, PL 11302</span></div>
    <div><svg width="12" height="12" viewBox="0 0 12 12"><path d="M2 1h3l1 3-2 1a7 7 0 0 0 3 3l1-2 3 1v3c0 1-1 1-2 1A10 10 0 0 1 1 3c0-1 0-2 1-2z" fill="#7ab82a"/></svg><span>23065100</span></div>
  </div>
  <ul class="fcol" style="left:421px">
    <h3>Company</h3>
    <li>About Us</li><li>GDPR</li><li>Investor Relations</li><li>Partners</li><li>Careers</li><li>Site Map</li>
  </ul>
  <ul class="fcol" style="left:589px">
    <h3>Company</h3>
    <li>Whitepaper &amp; Ebook</li><li>Webinars</li><li>Product Features</li><li>Blog</li><li>Go Mobile</li>
  </ul>
  <ul class="fcol" style="left:757px">
    <h3>Support and Contact</h3>
    <li>Contact Sales</li><li>24/7 Customer Support</li><li>FAQ</li>
  </ul>
  <div class="social"><span></span><span></span><span></span></div>
  <p class="copyright">© 2020 LoomTrax, Inc. All rights reserved.</p>
</footer>

</body>
</html>
```